Startup but Passionate F&B Company with big dreams for the future and multiple brands needs business

We need a simple logo and typography design for business card usage for a new company in a bustling and modern city called Brindle Terrace Pte Ltd. We are an F&B company that owns multiple brands of small boutique and indie cafes and eateries. We offer artisanal and home made food created with passion using quality and fresh ingredient. We would like to remain relevant and grow in the future constantly adapting changes and testing new boundaries with our menu and offerings in line with moving tastes and times. Final design and colors should be simple, fresh but modern and will remain relevant in time to come. For fonts we prefer modern fonts such as avenir (meaning future/futuristic) or any other new and trendy font types.
Updates

Please include a logo design as well as typography on th name card.

Thanks

Industry/Entity Type

Boutique

Font styles to use
Other font styles liked:
• Avenir or any other modern looking fonts

Colors

Designer to choose colors to be used in the design.

Requirements
Must have
• Logo + typography

```html
<!DOCTYPE html>
<html lang="en">
<head>
<meta charset="utf-8">
<title>Brindle Terrace Pte Ltd – Business Card</title>
<link rel="stylesheet" href="https://fonts.googleapis.com/css2?family=Exo+2:wght@400;500&display=swap">
<style>
  :root {
    --brand-blue: #3d3f94;
    --arc-grey: #38383d;
    --card-white: #ffffff;
    --card-shade: #eef0f2;
    --backdrop: #e6e7ea;
    --text-light: #ffffff;
  }
  * { margin: 0; padding: 0; box-sizing: border-box; }
  html, body { width: 1200px; height: 880px; overflow: hidden; }
  body {
    background: var(--backdrop);
    font-family: "Exo 2", sans-serif;
    position: relative;
  }
  .card {
    position: absolute;
    left: 280px;
    width: 640px;
    height: 366px;
    background: radial-gradient(ellipse at 60% 50%, var(--card-white) 40%, var(--card-shade) 100%);
    box-shadow: 0 6px 18px rgba(0,0,0,0.18);
    overflow: hidden;
  }
  .card--reverse { top: 48px; }
  .card--front { top: 466px; }

  .company-name {
    color: var(--brand-blue);
    font-weight: 400;
    font-size: 34px;
    letter-spacing: 1px;
    white-space: nowrap;
  }
  .card--reverse .company-name {
    position: absolute;
    left: 118px;
    top: 146px;
  }
  .web-band {
    position: absolute;
    right: 0;
    top: 250px;
    width: 300px;
    height: 28px;
    background: var(--brand-blue);
    clip-path: polygon(14px 0, 100% 0, 100% 100%, 0 100%);
    color: var(--text-light);
    font-size: 13px;
    line-height: 28px;
    padding-left: 58px;
  }

  .card-curve { position: absolute; inset: 0; }
  .contact-block {
    position: absolute;
    left: 36px;
    top: 30px;
    color: var(--text-light);
  }
  .person-name { font-size: 20px; font-weight: 500; letter-spacing: 1px; }
  .person-role { font-size: 13px; margin-top: 2px; }
  .address { font-size: 14px; line-height: 20px; margin-top: 34px; }
  .contact-list { list-style: none; margin-top: 22px; }
  .contact-list li {
    display: flex;
    align-items: center;
    gap: 10px;
    font-size: 13.5px;
    height: 24px;
  }
  .contact-list svg { width: 15px; height: 15px; flex: none; }
  .card--front .company-name {
    position: absolute;
    left: 334px;
    top: 166px;
    font-size: 25px;
    letter-spacing: 0.8px;
  }
</style>
</head>
<body>

  <section class="card card--reverse">
    <p class="company-name">Brindle Terrace Pte Ltd.</p>
    <p class="web-band">www.brindleterrace.com</p>
  </section>

  <section class="card card--front">
    <svg class="card-curve" viewBox="0 0 640 366" preserveAspectRatio="none" aria-hidden="true">
      <path d="M0 0 H386 Q262 104 256 366 H0 Z" fill="var(--arc-grey)" transform="translate(12 0)"/>
      <path d="M0 0 H378 Q254 104 248 366 H0 Z" fill="var(--brand-blue)"/>
    </svg>

    <div class="contact-block">
      <p class="person-name">MARCUS ELWOOD</p>
      <p class="person-role">Managing Director</p>
      <p class="address">047,12th floor,Harbour<br>Crest Road HCR</p>
      <ul class="contact-list">
        <li>
          <svg viewBox="0 0 16 16"><path d="M4 1 L6.5 4.5 L5 6.5 Q6.5 9.5 9.5 11 L11.5 9.5 L15 12 L13 15 Q5 14 1 3 Z" fill="#fff"/></svg>
          014 552 7310
        </li>
        <li>
          <svg viewBox="0 0 16 16"><rect x="4" y="1" width="8" height="14" rx="1.5" fill="none" stroke="#fff" stroke-width="1.5"/><circle cx="8" cy="12.5" r="0.9" fill="#fff"/></svg>
          014 552 7311
        </li>
        <li>
          <svg viewBox="0 0 16 16"><rect x="2" y="5" width="6" height="10" fill="#fff"/><rect x="8" y="2" width="6" height="13" fill="none" stroke="#fff" stroke-width="1.5"/></svg>
          014 552 7312
        </li>
        <li>
          <svg viewBox="0 0 16 16"><rect x="1" y="3" width="14" height="10" fill="#fff"/><path d="M1 3 L8 9 L15 3" fill="none" stroke="var(--brand-blue)" stroke-width="1.2"/></svg>
          hello@brindlemail.com
        </li>
        <li>
          <svg viewBox="0 0 16 16"><g fill="none" stroke="#fff" stroke-width="1.2"><circle cx="8" cy="8" r="6.5"/><ellipse cx="8" cy="8" rx="3" ry="6.5"/><path d="M1.5 8 H14.5 M2.5 4.8 H13.5 M2.5 11.2 H13.5"/></g></svg>
          www.brindleterrace.com
        </li>
      </ul>
    </div>

    <p class="company-name">Brindle Terrace Pte Ltd.</p>
  </section>

</body>
</html>
```